Criação de Logo e Papelaria (6 itens) para Equipamentos médico hospitalar
A empresa queria:
" Será uma empresa brasileira inovadora e empreendedora, que abrirá um mercado hoje dominado apenas pelas multinacionais. É uma empresa da área de saúde, voltada para atender o setor Médico no seguimento de diagnostico por imagem. Estamos inovando ao trazer para o Brasil uma nova tecnologia para criar a primeira e única Fabrica Brasileira de acessórios de Maquinas de Ultrassom. Fabricaremos o "Transdutor", que é o acessório da Maquina de Ultrassom que capta a imagem no exame e transmite á maquina para diagnostico do medico (Verificar a imagem do produto, Transdutor, anexada). O nosso produto será compatível e passível de uso nas maquinas de todos os grandes fabricantes multinacionais que atuam no mercado brasileiro. Tais como KV, Dravenor, Velunka entre outras. O nosso diferencial será, além de um produto brasileiro de alta qualidade, o rápido atendimento e assistência técnica local pelo fato da fabrica estar instalada no Brasil, mais especificamente na cidade de Ribeirao Preto, interior do estado de Sao Paulo, conhecido polo Tecnológico médico-hospitalar no Brasil de onde iremos explorar o mercado Brasileiro e Sul-americano. "

```html
<!DOCTYPE html>
<html lang="pt-BR">
<head>
<meta charset="utf-8">
<title>Sonavi — Papel Timbrado</title>
<link rel="stylesheet" href="https://fonts.googleapis.com/css2?family=Open+Sans:wght@600;700&display=swap">
<style>
  :root {
    --backdrop: #e9ebee;
    --paper: #ffffff;
    --brand-navy: #163a7a;
    --brand-blue: #2a6fc4;
    --watermark: #eef4fb;
    --ink: #1f2f55;
  }
  * { margin: 0; padding: 0; box-sizing: border-box; }
  html, body {
    width: 1200px; height: 1200px; overflow: hidden;
    background: var(--backdrop);
    font-family: "Open Sans", Arial, sans-serif;
  }
  .letterhead {
    position: absolute;
    left: 218px; top: 60px;
    width: 764px; height: 1080px;
    background: var(--paper);
    overflow: hidden;
    box-shadow: 0 6px 24px rgba(0,0,0,0.12);
  }
  .edge-band {
    position: absolute; top: 0; right: 0;
    width: 30px; height: 100%;
    background: var(--brand-navy);
  }
  .background-circle {
    position: absolute; left: -40px; top: 380px;
    width: 620px; height: 620px;
  }
  .brand {
    position: absolute; top: 42px; left: 0; right: 30px;
    display: flex; justify-content: center; align-items: center; gap: 10px;
  }
  .brand-dot {
    width: 26px; height: 26px; border-radius: 50%;
    background: var(--brand-blue);
  }
  .brand-name {
    font-size: 32px; font-weight: 700; color: var(--brand-blue);
    letter-spacing: 1px;
  }
  .contact {
    position: absolute; bottom: 34px; left: 0; right: 30px;
    text-align: center;
    font-size: 13px; font-weight: 600; line-height: 1.6;
    color: var(--ink);
  }
</style>
</head>
<body>
  <main class="letterhead">
    <svg class="background-circle" viewBox="0 0 620 620" aria-hidden="true">
      <circle cx="310" cy="310" r="280" fill="none" stroke="var(--watermark)" stroke-width="40"/>
    </svg>

    <header class="brand">
      <span class="brand-dot"></span>
      <span class="brand-name">Sonavi</span>
    </header>

    <footer class="contact">
      <p>Av. Serrano, 410 Jardim Alto · Ribeirão Preto SP</p>
      <p>16 4321-0000/16 4321-0101</p>
      <p>www.sonavi.com.br</p>
    </footer>

    <div class="edge-band"></div>
  </main>
</body>
</html>
```